Verdant Medispa Business Card

need a business card for our medispa, attached please see the logo.
our website is https://verdantmedispa-example.com

Sorina Belcourt, MD
Internal Medicine

555-204-7193

Sorina@verdantmedispa-example.com

Www.Verdantmedispa-example.com

738 E Harlow Blvd N, Ste 512, Katy, TX 77981

Target Market(s)

MedSpa, Cosmetics, Esthetics

Industry/Entity Type

MedicalSpa

Contact Information for Business Card

Please see the attached business card which i pulled from the internet. I like the idea back as a logo and front with info.

Font styles to use
Decorative

Requirements
Must have
• Color should be matching with Logo and Website theme, Also I like to have QR code for the website

```html
<!DOCTYPE html>
<html lang="en">
<head>
<meta charset="utf-8">
<title>Verdant Medispa Business Card</title>
<link href="https://fonts.googleapis.com/css2?family=Roboto:wght@400&display=swap" rel="stylesheet">
<style>
  :root {
    --backdrop: #4a423e;
    --card-brown: #5a3d2c;
    --card-white: #ffffff;
    --beige: #cdb39f;
    --ink: #4b3527;
    --qr-tone: #e6dbd2;
  }
  * { margin: 0; padding: 0; box-sizing: border-box; }
  html, body {
    width: 1200px; height: 1080px; overflow: hidden;
    background: var(--backdrop);
    font-family: "Roboto", Arial, sans-serif;
  }
  .canvas { position: relative; width: 1200px; height: 1080px; }
  .card {
    position: absolute; width: 584px; height: 334px;
    border-radius: 14px;
  }
  .card-front { left: 309px; top: 169px; background: var(--card-brown); }
  .card-back { left: 312px; top: 577px; background: var(--card-white); color: var(--ink); }

  .front-brand {
    position: absolute; left: 0; right: 0; top: 126px;
    text-align: center;
    font-size: 46px; font-weight: 400; letter-spacing: 1px;
    color: var(--beige);
  }
  .back-brand {
    position: absolute; left: 38px; top: 50px;
    font-size: 28px; font-weight: 400; color: var(--ink);
  }
  .person { position: absolute; right: 27px; top: 44px; text-align: right; }
  .person-name { font-size: 25px; line-height: 1.1; }
  .person-role { font-size: 15px; margin-top: 4px; }

  .contacts { position: absolute; left: 42px; top: 162px; }
  .contact-row {
    display: flex; align-items: center; gap: 9px;
    font-size: 15px; height: 23px; white-space: nowrap;
  }
  .contact-row svg { width: 16px; height: 16px; flex: none; }
  .divider {
    position: absolute; left: 340px; top: 163px;
    width: 1.5px; height: 68px; background: var(--ink);
  }
  .address {
    position: absolute; left: 354px; top: 162px;
    display: flex; gap: 9px; font-size: 15px; line-height: 19px;
    white-space: nowrap;
  }
  .address svg { width: 12px; height: 16px; flex: none; margin-top: 2px; }
  .appointment {
    position: absolute; left: 102px; top: 279px;
    display: flex; align-items: flex-end; font-size: 14px;
  }
  .leader {
    display: inline-block; width: 150px; margin: 0 2px 3px;
    border-bottom: 1.5px dotted var(--ink);
  }
  .qr-code {
    position: absolute; right: 27px; bottom: 26px;
    width: 62px; height: 62px;
    background: var(--qr-tone);
    border-radius: 3px;
  }
</style>
</head>
<body>
<main class="canvas">
  <section class="card card-front">
    <p class="front-brand">Verdant Medispa</p>
  </section>

  <section class="card card-back">
    <p class="back-brand">Verdant Medispa</p>

    <div class="person">
      <p class="person-name">Sorina Belcourt, MD</p>
      <p class="person-role">Internal Medicine</p>
    </div>

    <div class="contacts">
      <div class="contact-row">
        <svg viewBox="0 0 24 24" fill="var(--ink)"><path d="M6.6 10.8a15.1 15.1 0 0 0 6.6 6.6l2.2-2.2c.3-.3.7-.4 1-.2 1.1.4 2.3.6 3.6.6.6 0 1 .4 1 1V20c0 .6-.4 1-1 1A17 17 0 0 1 3 4c0-.6.4-1 1-1h3.5c.6 0 1 .4 1 1 0 1.3.2 2.5.6 3.6.1.3 0 .7-.2 1z"/></svg>
        <span>555-204-7193</span>
      </div>
      <div class="contact-row">
        <svg viewBox="0 0 24 24" fill="var(--ink)"><path d="M2 5h20v14H2z"/><path d="M2 5l10 8 10-8" fill="none" stroke="#fff" stroke-width="1.6"/></svg>
        <span>Sorina@verdantmedispa-example.com</span>
      </div>
      <div class="contact-row">
        <svg viewBox="0 0 24 24" fill="none" stroke="var(--ink)" stroke-width="1.5"><circle cx="12" cy="12" r="9"/><ellipse cx="12" cy="12" rx="4" ry="9"/><path d="M3 12h18M4.5 7.5h15M4.5 16.5h15"/></svg>
        <span>Www.Verdantmedispa-example.com</span>
      </div>
    </div>

    <div class="divider"></div>

    <div class="address">
      <svg viewBox="0 0 16 22" fill="var(--ink)"><path d="M8 0a8 8 0 0 0-8 8c0 6 8 14 8 14s8-8 8-14a8 8 0 0 0-8-8zm0 11a3 3 0 1 1 0-6 3 3 0 0 1 0 6z"/></svg>
      <p>738 E Harlow Blvd N, Ste 512,<br>Katy, TX 77981</p>
    </div>

    <div class="appointment">
      <span>Date</span><span class="leader"></span><span>Time</span><span class="leader"></span>
    </div>

    <div class="qr-code" role="img" aria-label="QR code linking to the Verdant Medispa website"></div>
  </section>
</main>
</body>
</html>
```